Corporate Dinner Invite at Verolla for PMV

PMV is hosting a corporate dinner at the BRQ Conference and we need an email attachment invite for the event. Please use some images from this site for inspiration: https://www.verollaexample.com/fernparlor/

Invite Title:
Join us for dinner!

Event Details:
Tuesday, October 24th 2023 at 6:30pm
Verolla Chicago, Fern Parlor
347 W Harlow Ave, Chicago, IL 60622

Target Market(s)

Corporate Audience

Font styles to use
Script

Colors
0054AA
0677BA
7BADD7
CADEEF
E8F1F8

Requirements
Must have
• PMV logo, event date / time, event location details, photo(s) from Fern Parlor

```html
<!DOCTYPE html>
<html lang="en">
<head>
<meta charset="utf-8">
<title>PMV Dinner Invitation</title>
<link href="https://fonts.googleapis.com/css2?family=Yellowtail&family=Kaushan+Script&family=Cormorant+Garamond:ital,wght@1,500;1,600&family=Montserrat:wght@700&display=swap" rel="stylesheet">
<style>
  :root{
    --indigo:#3d3f96;
    --cyan:#1aa9e0;
    --gold:#e0b45a;
    --paper:#ffffff;
    --photo-warm:#6b4a2a;
    --photo-dark:#2a1c12;
  }
  html,body{margin:0;padding:0;overflow:hidden;background:var(--paper);}
  .invite{position:relative;width:915px;height:1200px;background:var(--paper);overflow:hidden;}
  .brand{position:absolute;left:0;width:915px;top:128px;display:flex;justify-content:center;align-items:center;gap:14px;}
  .brand-mark{width:46px;height:46px;background:var(--indigo);}
  .brand-name{font-family:'Cormorant Garamond',serif;font-style:italic;font-weight:600;font-size:72px;color:var(--indigo);line-height:1;}
  .headline-lead{position:absolute;left:492px;top:328px;font-family:'Kaushan Script',cursive;font-size:58px;color:var(--gold);line-height:1;transform:rotate(-6deg);transform-origin:left center;}
  .headline{position:absolute;left:150px;top:322px;width:640px;text-align:center;font-family:'Yellowtail',cursive;font-size:190px;line-height:1;color:var(--indigo);text-shadow:4px 5px 0 var(--cyan);transform:rotate(-4deg);}
  .photo{position:absolute;border:5px solid var(--paper);box-shadow:2px 3px 8px rgba(0,0,0,.3);}
  .photo-drinks{left:100px;top:590px;width:260px;height:160px;transform:rotate(14deg);background:linear-gradient(160deg,#3b2414,#8a5a2a 55%,#d8d2c8);}
  .photo-dining{left:338px;top:592px;width:250px;height:160px;transform:rotate(15deg);background:linear-gradient(150deg,#4a3422,#7a5a3a 50%,#cfc5b6);}
  .photo-bar{left:512px;top:582px;width:270px;height:178px;transform:rotate(15deg);background:linear-gradient(135deg,var(--photo-dark),#8a6234 55%,var(--photo-warm));}
  .event-at{position:absolute;left:0;width:915px;top:808px;text-align:center;font-family:'Cormorant Garamond',serif;font-style:italic;font-weight:600;font-size:36px;color:var(--cyan);}
  .event-at small{font-size:20px;}
  .details{position:absolute;left:218px;top:872px;list-style:none;margin:0;padding:0;font-family:'Cormorant Garamond',serif;font-style:italic;font-weight:600;color:var(--indigo);font-size:37px;line-height:1.15;}
  .details li{display:flex;align-items:flex-start;gap:12px;margin-bottom:6px;}
  .details svg{flex:none;margin-top:6px;}
  .see-you{position:absolute;left:0;width:915px;top:1060px;text-align:center;font-family:'Yellowtail',cursive;font-size:76px;color:var(--indigo);}
</style>
</head>
<body>
<main class="invite">
  <div class="brand"><span class="brand-mark"></span><span class="brand-name">PMV</span></div>

  <div class="headline-lead">Join us for</div>
  <h1 class="headline" style="margin:0;font-weight:400;">Dinner</h1>

  <div class="photo photo-drinks" role="img" aria-label="Photo of cocktails lined up on the bar at Fern Parlor"></div>
  <div class="photo photo-dining" role="img" aria-label="Photo of the candlelit dining room at Fern Parlor"></div>
  <div class="photo photo-bar" role="img" aria-label="Photo of the lounge bar and seating at Fern Parlor"></div>

  <div class="event-at"><small>@</small> BRQ Conference</div>

  <ul class="details">
    <li>
      <svg width="28" height="30" viewBox="0 0 28 30" aria-hidden="true"><rect x="1" y="4" width="26" height="25" fill="var(--gold)"/><rect x="4" y="11" width="20" height="15" fill="#f3dcae"/><rect x="6" y="1" width="3" height="6" fill="var(--gold)"/><rect x="19" y="1" width="3" height="6" fill="var(--gold)"/></svg>
      <span>Tuesday, October 24th, 2023</span>
    </li>
    <li>
      <svg width="28" height="28" viewBox="0 0 28 28" aria-hidden="true"><circle cx="14" cy="14" r="12" fill="none" stroke="var(--gold)" stroke-width="2.5"/><path d="M14 7v8l5 4" fill="none" stroke="var(--gold)" stroke-width="2.5" stroke-linecap="round"/></svg>
      <span>6:30pm</span>
    </li>
    <li>
      <svg width="28" height="28" viewBox="0 0 28 28" aria-hidden="true"><circle cx="14" cy="14" r="12" fill="none" stroke="var(--gold)" stroke-width="2.5"/><path d="M14 21s-5-5-5-8.5a5 5 0 0 1 10 0C19 16 14 21 14 21z" fill="none" stroke="var(--gold)" stroke-width="2"/><circle cx="14" cy="12.5" r="1.8" fill="var(--gold)"/></svg>
      <span>Verolla Chicago, Fern Parlor<br>347 W Harlow Ave, Chicago, IL 60622</span>
    </li>
  </ul>

  <div class="see-you">See You There!</div>
</main>
</body>
</html>
```